first fantastic look and impression

We are looking for a concept for letterhead, business card, emailfooter and template for invoices or offers for our company in the consultation business.
The dancer is a symbol who we are: it looks simple, but there is a lot of hard work and many years of training in this movement. The look is also what we want: elegant, modern, strong, with a touch of extravaganza
Target Market(s)
Hotelbusiness , Consulting
Font styles to use
Sans Serif
Other font styles liked:
- please give us a option we are open
Requirements
Must have
- We are not typical consultants but sparring partners and coaches for the hotel and that should also be expressed in the design. Maybe there is an icon that supports the whole thing. We are more modern and bolder than our industry colleagues.
we are modern, fresh, agile, fast
Nice to have
- a icon

```html
<!DOCTYPE html>
<html lang="en">
<head>
<meta charset="utf-8">
<title>Halvorsen+Partner — Letterhead</title>
<link rel="stylesheet" href="https://fonts.googleapis.com/css2?family=Open+Sans:wght@400;700&display=swap">
<style>
  :root {
    --backdrop: #d9dcde;
    --paper: #ffffff;
    --brand-blue: #4f6f91;
    --brand-blue-light: #8aa2bb;
    --text-grey: #6d6e70;
    --silhouette-top: #e4e6e9;
    --silhouette-bottom: #f1f2f4;
  }
  * { margin: 0; padding: 0; box-sizing: border-box; }
  html, body {
    width: 1200px;
    height: 784px;
    overflow: hidden;
    background: var(--backdrop);
    font-family: "Open Sans", Arial, sans-serif;
  }
  .letterhead {
    position: absolute;
    left: 330px;
    top: 22px;
    width: 540px;
    height: 740px;
    background: var(--paper);
    box-shadow: 0 4px 14px rgba(0,0,0,0.12);
  }
  .header-band {
    position: absolute;
    left: 0;
    right: 0;
    top: 26px;
    height: 14px;
    background: linear-gradient(180deg, var(--brand-blue) 0%, var(--brand-blue-light) 100%);
  }
  .brand-name {
    position: absolute;
    right: 40px;
    top: 58px;
    font-size: 19px;
    font-weight: 400;
    color: var(--brand-blue);
    letter-spacing: 0.3px;
  }
  .dancer-watermark {
    position: absolute;
    left: 120px;
    top: 250px;
    width: 250px;
    height: 230px;
    border-radius: 46% 54% 40% 60% / 55% 45% 55% 45%;
    background: radial-gradient(ellipse at 45% 45%, var(--silhouette-top) 0%, var(--silhouette-bottom) 70%, rgba(255,255,255,0) 100%);
  }
  .contact-block {
    position: absolute;
    right: 36px;
    top: 300px;
    width: 170px;
  }
  .contact-divider {
    display: block;
    margin-bottom: 6px;
  }
  .contact-line {
    display: flex;
    align-items: center;
    gap: 5px;
    font-size: 9.5px;
    line-height: 14px;
    color: var(--text-grey);
  }
  .contact-line.location {
    font-weight: 700;
    color: var(--brand-blue);
  }
  .contact-icon { flex: none; }
</style>
</head>
<body>
  <main class="letterhead">
    <div class="header-band"></div>

    <div class="brand-name">Halvorsen+Partner</div>

    <div class="dancer-watermark" role="img" aria-label="Faint photograph of a dancer in a flowing dress, crouched mid-movement"></div>

    <address class="contact-block">
      <svg class="contact-divider" width="170" height="22" viewBox="0 0 170 22">
        <line x1="0" y1="21" x2="50" y2="1" stroke="#c9ced4" stroke-width="0.8"/>
      </svg>
      <div class="contact-line location">
        <svg class="contact-icon" width="9" height="9" viewBox="0 0 10 10">
          <circle cx="5" cy="5" r="5" fill="#4f6f91"/>
          <path d="M5 2.2a1.8 1.8 0 0 1 1.8 1.8c0 1.4-1.8 3.6-1.8 3.6S3.2 5.4 3.2 4A1.8 1.8 0 0 1 5 2.2z" fill="#fff"/>
        </svg>
        Brenntal/Austria
      </div>
      <div class="contact-line">
        <svg class="contact-icon" width="9" height="9" viewBox="0 0 10 10">
          <circle cx="5" cy="5" r="5" fill="#4f6f91"/>
          <rect x="2.5" y="3.2" width="5" height="3.6" fill="none" stroke="#fff" stroke-width="0.8"/>
          <path d="M2.5 3.4L5 5.3 7.5 3.4" fill="none" stroke="#fff" stroke-width="0.8"/>
        </svg>
        info@halvorsenpartner.com
      </div>
      <div class="contact-line">
        <svg class="contact-icon" width="9" height="9" viewBox="0 0 10 10">
          <circle cx="5" cy="5" r="5" fill="#4f6f91"/>
          <circle cx="5" cy="5" r="2.6" fill="none" stroke="#fff" stroke-width="0.7"/>
          <line x1="2.4" y1="5" x2="7.6" y2="5" stroke="#fff" stroke-width="0.6"/>
        </svg>
        halvorsenpartner.com
      </div>
    </address>
  </main>
</body>
</html>
```